Business Card for Field Lotus-Eco Friendly Organic Clothing Brand

We are looking for an amazing business card for our eco friendly, organic clothing brand. We are thinking maybe a business card with a peel off sticker on the back, since our hanging clothing tag is a peel off sticker on the back. I will attach our hang tag so we can make sure we stay in line with our design. I've also attached a bag we are doing because I do like the scattered emblem look as well.

```html
<!DOCTYPE html>
<html lang="en">
<head>
<meta charset="utf-8">
<title>Field Lotus Business Card</title>
<link href="https://fonts.googleapis.com/css2?family=Arimo:wght@400;700&family=Tinos:wght@700&display=swap" rel="stylesheet">
<style>
  :root {
    --page: #ece9e4;
    --card: #ffffff;
    --green: #1e6a3c;
    --pink: #e3127f;
    --white: #ffffff;
  }
  html, body {
    margin: 0;
    width: 1200px;
    height: 902px;
    overflow: hidden;
    background: var(--page);
  }
  .business-card {
    position: absolute;
    left: 80px;
    top: 154px;
    width: 1040px;
    height: 594px;
    background: var(--card);
    box-shadow: 0 6px 24px rgba(0,0,0,0.18);
    overflow: hidden;
  }
  .card-wave {
    position: absolute;
    inset: 0;
  }
  .brand {
    position: absolute;
    left: 230px;
    top: 104px;
    display: flex;
    align-items: center;
    gap: 24px;
  }
  .brand-dot {
    width: 88px;
    height: 88px;
    border-radius: 50%;
    background: var(--green);
  }
  .brand-name {
    font-family: "Arimo", Arial, sans-serif;
    font-weight: 700;
    font-size: 72px;
    line-height: 1;
    color: var(--pink);
    letter-spacing: 1px;
  }
  .holder {
    position: absolute;
    left: 50px;
    top: 478px;
    color: var(--white);
  }
  .holder-name {
    font-family: "Tinos", "Times New Roman", serif;
    font-weight: 700;
    font-size: 44px;
    line-height: 1;
  }
  .holder-title {
    font-family: "Arimo", Arial, sans-serif;
    font-size: 27px;
    margin-top: 6px;
  }
  .contact {
    position: absolute;
    left: 606px;
    top: 404px;
    padding: 0 0 0 26px;
    border-left: 2px solid var(--white);
    list-style: none;
    margin: 0;
    font-family: "Arimo", Arial, sans-serif;
    font-size: 24px;
    color: var(--white);
  }
  .contact li {
    display: flex;
    align-items: center;
    gap: 22px;
    height: 42px;
  }
  .contact-icon {
    width: 24px;
    height: 24px;
    flex: none;
  }
</style>
</head>
<body>
  <div class="business-card">
    <svg class="card-wave" width="1040" height="594" viewBox="0 0 1040 594">
      <path d="M0,404 C300,446 560,400 740,290 C860,215 960,180 1040,170 L1040,594 L0,594 Z" fill="var(--pink)"/>
      <path d="M0,430 C300,472 560,426 740,316 C860,241 960,206 1040,196 L1040,594 L0,594 Z" fill="var(--green)"/>
    </svg>

    <div class="brand">
      <span class="brand-dot"></span>
      <span class="brand-name">Field Lotus</span>
    </div>

    <div class="holder">
      <div class="holder-name">Dana Morrow</div>
      <div class="holder-title">Managing Director</div>
    </div>

    <ul class="contact">
      <li>
        <svg class="contact-icon" viewBox="0 0 24 24"><rect width="24" height="24" rx="3" fill="#fff"/><path d="M7 5l3 3-2 2c1 2 3 4 5 5l2-2 3 3-2 3C10 19 5 14 4 8z" fill="var(--green)"/></svg>
        <span>(555) 214-7702</span>
      </li>
      <li>
        <svg class="contact-icon" viewBox="0 0 24 24"><rect width="24" height="24" rx="3" fill="#fff"/><path d="M12 4a5 5 0 0 0-5 5c0 4 5 11 5 11s5-7 5-11a5 5 0 0 0-5-5z" fill="var(--green)"/><circle cx="12" cy="9" r="2" fill="#fff"/></svg>
        <span>Harbor Vale, FL&nbsp; 33012</span>
      </li>
      <li>
        <svg class="contact-icon" viewBox="0 0 24 24"><rect width="24" height="24" rx="3" fill="#fff"/><circle cx="12" cy="12" r="7" fill="none" stroke="var(--green)" stroke-width="2"/><path d="M5 12h14M12 5c-3 4-3 10 0 14M12 5c3 4 3 10 0 14" fill="none" stroke="var(--green)" stroke-width="1.5"/></svg>
        <span>www.fieldlotus.com</span>
      </li>
      <li>
        <svg class="contact-icon" viewBox="0 0 24 24"><rect width="24" height="24" rx="3" fill="#fff"/><rect x="5" y="7" width="14" height="10" fill="none" stroke="var(--green)" stroke-width="2"/><path d="M5 7l7 6 7-6" fill="none" stroke="var(--green)" stroke-width="2"/></svg>
        <span>hello@fieldlotus.com</span>
      </li>
    </ul>
  </div>
</body>
</html>
```